Graphic Design for a Info Card

We would like a graphic design for an info card . We would like the colours to correspond to our logo , you can add in the colours navy blue or yellow if you would like. We would like it to have the following information. We want something that really pops. We would like the size to be 4 1/2 x 6 .

ATTENTION!! Delivery Promo! Order from us on the @hopplemeals app or @marlinrunner app on FRIDAYS and receive a FREE Sample of our one of our meal prep meals in your bag!
DID YOU KNOW?! Meal Prep is another great service that we offer. Saving you time, promoting your health, and best of all providing a delicious lunch . You can find more info on our website www.brivoranpantry.example . All orders are available for delivery or pickup!

```html
<!DOCTYPE html>
<html lang="en">
<head>
<meta charset="utf-8">
<title>Brivoran Pantry – Delivery Promo Card</title>
<link rel="stylesheet" href="https://fonts.googleapis.com/css2?family=Montserrat:wght@500;600;700;800;900&display=swap">
<style>
  :root {
    --royal: #1f2fd6;
    --navy: #0c137a;
    --deep: #070b52;
    --yellow: #ffe21a;
    --lime: #d6e83a;
    --white: #ffffff;
    --ink: #1b1f3a;
    --green: #7cb342;
    --grey: #6d7178;
  }
  * { box-sizing: border-box; margin: 0; padding: 0; }
  html, body { width: 675px; height: 1200px; overflow: hidden; background: #eef0ee; }
  body { font-family: "Montserrat", sans-serif; }

  .card {
    position: relative;
    width: 675px;
    height: 1200px;
    background: var(--white);
    overflow: hidden;
  }
  .promo-panel {
    position: absolute;
    inset: 0 0 250px 0;
    background:
      radial-gradient(ellipse 70% 45% at 50% 28%, #3a4cff 0%, var(--royal) 40%, var(--navy) 78%, var(--deep) 100%);
    text-align: center;
    color: var(--white);
  }
  .attention-art {
    position: absolute;
    left: 90px;
    top: 40px;
    width: 495px;
    height: 410px;
  }
  .section-title {
    position: absolute;
    left: 0; right: 0;
    font-weight: 900;
    font-size: 38px;
    letter-spacing: 0.5px;
    color: var(--yellow);
    text-transform: uppercase;
  }
  .section-body {
    position: absolute;
    left: 85px; right: 85px;
    font-weight: 500;
    font-size: 19px;
    line-height: 1.45;
  }
  .handle { color: var(--yellow); font-weight: 700; }
  .delivery-title { top: 478px; }
  .delivery-body { top: 530px; }
  .know-title { top: 652px; }
  .know-body { top: 704px; }

  .website-strip {
    position: absolute;
    left: 75px; right: 75px;
    top: 812px;
    height: 38px;
    display: flex;
    align-items: stretch;
    font-size: 16px;
    font-weight: 700;
  }
  .website-strip .lead {
    flex: 1;
    background: var(--lime);
    color: var(--ink);
    display: flex; align-items: center; justify-content: center;
  }
  .website-strip .url {
    background: var(--white);
    color: var(--ink);
    padding: 0 16px;
    display: flex; align-items: center;
  }
  .availability {
    position: absolute;
    left: 0; right: 0;
    top: 880px;
    font-size: 18px;
    font-weight: 600;
  }

  .brand-band {
    position: absolute;
    left: 0; right: 0; bottom: 0;
    height: 250px;
    display: flex;
    align-items: center;
    justify-content: center;
    gap: 14px;
  }
  .brand-mark {
    width: 22px; height: 22px;
    border-radius: 50%;
    background: var(--green);
  }
  .brand-name {
    font-weight: 800;
    font-size: 46px;
    color: var(--grey);
    letter-spacing: 1px;
    text-transform: uppercase;
  }
</style>
</head>
<body>
  <main class="card">
    <section class="promo-panel">
      <svg class="attention-art" viewBox="0 0 495 410" role="img" aria-label="Illustration: speech bubble with the word ATTENTION and a blue megaphone with yellow sound lines">
        <defs>
          <radialGradient id="bubbleGlow" cx="50%" cy="45%" r="60%">
            <stop offset="0%" stop-color="#5fb4ff"/>
            <stop offset="100%" stop-color="#2f7be8"/>
          </radialGradient>
        </defs>
        <rect x="40" y="70" width="415" height="240" rx="60" fill="url(#bubbleGlow)" opacity="0.9"/>
      </svg>

      <h2 class="section-title delivery-title">Delivery Promo!</h2>
      <p class="section-body delivery-body">
        Order from us on the <span class="handle">@hopplemeals app</span> or <span class="handle">@marlinrunner app</span> on FRIDAYS and receive a FREE Sample of our one of our meal prep meals in your bag!
      </p>

      <h2 class="section-title know-title">Did you know?</h2>
      <p class="section-body know-body">
        Meal Prep is another great service that we offer. Saving you time, promoting your health, and best of all providing a delicious lunch.
      </p>

      <div class="website-strip">
        <span class="lead">You can find more info on our website:</span>
        <span class="url">www.brivoranpantry.example</span>
      </div>

      <p class="availability">All orders are available for delivery or pickup!</p>
    </section>

    <footer class="brand-band">
      <span class="brand-mark"></span>
      <span class="brand-name">Brivoran Pantry</span>
    </footer>
  </main>
</body>
</html>
```